Titans of Dirt Z event poster / flyer

Looking for an event flyer designed.
Looking for a 1987 theme for a 2 stroke motocross race. Would like to copy the 1987 giants of sound flyer.
On the poster where it says 1987 putting a slash through it. And putting our date of June 7th - june 9 th. 2024 on it .
Schedule will be
Friday june 7th, 2 stroke practice
Show and shine Friday after practice (bike show)
Also, would like to promote a live 80s band Friday night.
titans of dirt z race Saturday june 8th
(2 stroke only.)
2 stroke straight rhythm event Saturday night under the lights.
Sunday QTV june 9th
2 stroke and 4 stroke race.
On part of the flyer, I would like to use this copper raven image, holding some balls of steel. One idea do you have balls of steel?
Our premier class will be themed the storm rider 500 two-stroke big bore class. We Would like to advertise that all who dare race a big bore 2 stroke are sponsored. No race fee for this class.
Trophy & Awards podium celebration, Saturday after the event.
$5,000 added pro purse plus 100% payback
For 125cc and 250cc pro classes
Website www.titansofdirtz-example.com
Images the Velkor with number six on it would be a good advertisement for the show and shine.
I think the number 98 going through the turn on the green bike would be great to add as a photo on the flyer.

```html
<!DOCTYPE html>
<html lang="en">
<head>
<meta charset="utf-8">
<title>Titans of Dirt Z – 2 Stroke Straight Rhythm Event</title>
<link rel="stylesheet" href="https://fonts.googleapis.com/css2?family=Anton&family=Exo+2:wght@600;700;800&family=Russo+One&display=swap">
<style>
  :root {
    --backdrop: #f2f2f2;
    --field-dark: #173a2e;
    --field-mid: #2b6a50;
    --field-light: #5d8f6e;
    --signal-yellow: #f3ea1c;
    --race-red: #e3202a;
    --ink: #0d0d0d;
    --paper: #ffffff;
  }
  * { margin: 0; padding: 0; box-sizing: border-box; }
  html, body { width: 1200px; height: 1200px; overflow: hidden; background: var(--backdrop); }
  .flyer {
    position: absolute; left: 231px; top: 77px; width: 738px; height: 1044px;
    overflow: hidden; font-family: "Exo 2", sans-serif; color: var(--paper);
  }
  .flyer__photo {
    position: absolute; inset: 0;
    background:
      radial-gradient(ellipse at 30% 45%, var(--field-light) 0%, transparent 55%),
      radial-gradient(ellipse at 70% 80%, #3f7a5c 0%, transparent 50%),
      linear-gradient(160deg, var(--field-mid) 0%, var(--field-dark) 100%);
  }
  .flyer__sponsor {
    position: absolute; left: 414px; top: 70px; width: 212px; height: 170px;
    background: var(--ink); display: flex; align-items: center; justify-content: center;
    font-family: "Russo One", sans-serif; font-size: 24px; color: var(--race-red);
    letter-spacing: 1px;
  }
  .title-numeral {
    position: absolute; left: 128px; top: 170px;
    font-family: "Anton", sans-serif; font-size: 300px; line-height: 1;
    color: var(--signal-yellow); transform: skewX(-10deg);
    -webkit-text-stroke: 5px var(--ink); paint-order: stroke fill;
  }
  .title-word {
    position: absolute; left: 248px; top: 318px;
    font-family: "Russo One", sans-serif; font-style: italic; font-size: 80px; line-height: 1;
    color: var(--race-red); transform: skewX(-14deg);
    -webkit-text-stroke: 2px var(--paper); paint-order: stroke fill;
  }
  .event-name, .event-sub, .event-day {
    position: absolute; left: 0; width: 738px; text-align: center; padding-left: 140px;
  }
  .event-name { top: 456px; font-size: 29px; font-weight: 700; letter-spacing: 0.5px; }
  .event-sub { top: 494px; font-size: 18px; font-weight: 700; letter-spacing: 0.5px; }
  .event-day { top: 538px; font-size: 40px; font-weight: 800; color: var(--signal-yellow); }
  .right-info { position: absolute; right: 34px; text-align: right; font-weight: 700; }
  .race-format { top: 607px; font-size: 35px; letter-spacing: 0.5px; }
  .awards { top: 675px; font-size: 22px; line-height: 31px; }
  .pro-classes { top: 800px; font-size: 27px; line-height: 35px; }
  .website { top: 974px; font-size: 17px; }
  .purse-panel { position: absolute; left: 0; top: 0; }
  .purse {
    position: absolute; left: 54px; color: var(--ink); font-weight: 700;
  }
  .purse__amount { top: 833px; font-family: "Russo One", sans-serif; font-size: 54px; }
  .purse__line { font-size: 19px; }
  .purse__line--one { top: 898px; }
  .purse__line--two { top: 935px; }
</style>
</head>
<body>
<main class="flyer">
  <div class="flyer__photo" role="img" aria-label="Motocross riders racing through a dirt turn, green-toned action photos"></div>

  <div class="flyer__sponsor">COPPER RAVEN</div>

  <div class="title-numeral">2</div>
  <div class="title-word">STROKE</div>

  <div class="event-name">STRAIGHT RHYTHM EVENT</div>
  <div class="event-sub">SATURDAY NIGHT UNDER THE LIGHTS</div>
  <div class="event-day">Sunday QTV june 9th</div>

  <div class="right-info race-format">2 stroke and 4 stroke race</div>
  <div class="right-info awards">Trophy &amp; Awards<br>podium celebration,<br>Saturday after the event</div>
  <div class="right-info pro-classes">125cc and<br>250cc pro classes</div>

  <svg class="purse-panel" width="738" height="1044" viewBox="0 0 738 1044" aria-hidden="true">
    <polygon points="0,629 338,798 338,1044 0,1044" fill="var(--signal-yellow)"/>
  </svg>
  <div class="purse purse__amount">$5,000</div>
  <div class="purse purse__line purse__line--one">added pro purse plus</div>
  <div class="purse purse__line purse__line--two">100% payback</div>

  <div class="right-info website">www.titansofdirtz-example.com</div>
</main>
</body>
</html>
```